Etiketten-Design für Honiggläser
Zielgruppe
Imkerei Wendler
Wir sind eine Familienbetrieb und vertreiben hochwertigen Honig aus eigener Imkerei
Aufgabenstellung
Es werden Etiketten für Honiggläser benötigt
Es gibt drei verschiedene Größen von Gläser (siehe Anhang) und je größe einmal „Frühtracht“ und einmal „Sommertracht“
Also insgesamt 6 Etiketten
500g Frühtracht und Sommertracht
250g Frühtracht und Sommertracht
150g Frühtracht und Sommertracht

```html
<!DOCTYPE html>
<html lang="de">
<head>
<meta charset="utf-8">
<title>Imkerei Wendler – Honigetiketten</title>
<link rel="stylesheet" href="https://fonts.googleapis.com/css2?family=Alex+Brush&family=Open+Sans:wdth,wght@75..100,300..700&display=swap">
<style>
  :root {
    --paper: #f2e0b6;
    --paper-dark: #e9d3a3;
    --green: #8cbc40;
    --green-soft: #a9c77a;
    --orange: #e08c2c;
    --orange-soft: #eba271;
    --ink: #1c1a17;
    --field: #dfdca6;
    --bg: #ffffff;
  }
  html, body { margin: 0; padding: 0; overflow: hidden; background: var(--bg); }
  .canvas {
    position: relative;
    width: 1200px; height: 910px;
    overflow: hidden;
    background: var(--bg);
    font-family: "Open Sans", Arial, sans-serif;
    color: var(--ink);
  }

  /* Lid sticker: circle with tab */
  .lid-sticker { position: absolute; top: 18px; width: 182px; height: 290px; }
  .lid-sticker .disc {
    position: absolute; left: 0; top: 0;
    width: 182px; height: 182px; border-radius: 50%;
    box-sizing: border-box; border: 10px solid var(--accent);
    background: var(--paper);
    display: flex; align-items: center; justify-content: center;
  }
  .lid-sticker .tab {
    position: absolute; left: 57px; top: 166px;
    width: 68px; height: 124px;
    box-sizing: border-box;
    border-left: 8px solid var(--accent); border-right: 8px solid var(--accent);
    background: var(--paper);
    text-align: center;
  }
  .lid-sticker .claim {
    margin-top: 38px;
    font-size: 8px; line-height: 10px; font-weight: 500;
    color: var(--accent-text);
  }
  .lid-sticker .weight { margin-top: 8px; font-size: 16px; font-weight: 600; }

  .brand {
    font-family: "Open Sans", Arial, sans-serif;
    font-weight: 600;
    color: var(--accent-text);
    text-align: center;
    white-space: nowrap;
  }
  .lid-sticker .brand { font-size: 17px; line-height: 20px; }

  .theme-green { --accent: var(--green); --accent-text: #76a92d; --accent-soft: var(--green-soft); }
  .theme-orange { --accent: var(--orange); --accent-text: #e2852a; --accent-soft: var(--orange-soft); }

  /* Front band label */
  .front-label {
    position: absolute; top: 326px;
    width: 304px; height: 170px;
    background: var(--paper);
    overflow: hidden;
  }
  .front-label .brand { position: absolute; top: 18px; left: 0; right: 0; font-size: 18px; }
  .script {
    font-family: "Alex Brush", cursive;
    font-weight: 400;
    color: var(--ink);
    text-align: center;
    white-space: nowrap;
  }
  .front-label .script { position: absolute; top: 50px; left: 0; right: 0; font-size: 46px; line-height: 60px; }
  .comb-band {
    position: absolute; left: 0; right: 0; bottom: 0;
    background: linear-gradient(to top, var(--accent-soft), rgba(0,0,0,0));
    opacity: .75;
  }
  .front-label .comb-band { height: 42px; }

  /* Wrap-around label */
  .wrap-label {
    position: absolute; left: 74px; top: 617px;
    width: 1057px; height: 242px;
    background: var(--paper);
    overflow: hidden;
  }
  .wrap-label .comb-band { height: 70px; }
  .producer {
    position: absolute; left: 30px; top: 13px;
    font-stretch: 75%; font-weight: 400;
    font-size: 15px; line-height: 18px;
  }
  .producer p { margin: 0 0 18px; }
  .producer .web { font-weight: 700; }
  .producer .net { font-size: 36px; line-height: 40px; font-stretch: 85%; margin-top: -6px; }
  .wrap-label .brand { position: absolute; top: 40px; left: 360px; width: 332px; font-size: 30px; }
  .wrap-label .script { position: absolute; top: 82px; left: 360px; width: 332px; font-size: 76px; line-height: 100px; }
  .batch-fields { position: absolute; left: 798px; top: 11px; width: 226px; }
  .batch-fields .field-label { font-stretch: 75%; font-size: 15px; line-height: 18px; }
  .batch-fields .field { height: 41px; background: var(--field); margin: 5px 0 10px; }
</style>
</head>
<body>
<div class="canvas">

  <div class="lid-sticker theme-green" style="left: 329px;">
    <div class="disc"><div class="brand">Imkerei Wendler</div></div>
    <div class="tab">
      <div class="claim">ECHTER<br>DEUTSCHER<br>HONIG</div>
      <div class="weight">500g</div>
    </div>
  </div>

  <div class="lid-sticker theme-orange" style="left: 705px;">
    <div class="disc"><div class="brand">Imkerei Wendler</div></div>
    <div class="tab">
      <div class="claim">ECHTER<br>DEUTSCHER<br>HONIG</div>
      <div class="weight">500g</div>
    </div>
  </div>

  <div class="front-label theme-green" style="left: 268px;">
    <div class="brand">Imkerei Wendler</div>
    <div class="script">Frühtracht</div>
    <div class="comb-band" role="img" aria-label="Grünes Wabenmuster am unteren Rand"></div>
  </div>

  <div class="front-label theme-orange" style="left: 644px;">
    <div class="brand">Imkerei Wendler</div>
    <div class="script">Sommertracht</div>
    <div class="comb-band" role="img" aria-label="Oranges Wabenmuster am unteren Rand"></div>
  </div>

  <div class="wrap-label theme-green">
    <div class="comb-band" role="img" aria-label="Grünes Wabenmuster am unteren Rand"></div>
    <div class="producer">
      <p>Hergestellt in der Deutschland</p>
      <p>Imkerei Jonas Wendler<br>Lindenweg 4 - 31655 Bergwiesen<br><span class="web">www.imkereiwendler.de</span></p>
      <p>Kühl und trocken lagern!</p>
      <div class="net">250g</div>
    </div>
    <div class="brand">Imkerei Wendler</div>
    <div class="script">Frühtracht</div>
    <div class="batch-fields">
      <div class="field-label">Los-No.:</div>
      <div class="field"></div>
      <div class="field-label">Mindestens haltbar bis:</div>
      <div class="field"></div>
      <div class="field-label">Datum der Honigernte:</div>
      <div class="field"></div>
    </div>
  </div>

</div>
</body>
</html>
```